Fahrzeugbeschriftung für Elektrofirma
Zielgruppe
Wir sind eine Elektrofirma und suchen ein hochwertiges Design, unsere Ziehlgruppe sind smarthome bewuste Familen oder Männner.
Aufgabenstellung
Wir haben varelle Toriv L1 H2 und vastrano L1 H2,
So ähnlich wie bei Lutz & Baier
Hinten: - Gebäudetechnik , - Smarthome, - Sicherheitstechnik,
Telefonnummer 02087 3519284
Facebook: ElektroTannreuter
Instagram: elektro_tannreuter
Seiten: Ahornweg 17
47128 Dinslaken
Seiten hinten: Logo mit Tannreuter Elektro- und Datentechnik
www.elektro-tannreuter-beispiel.de, info@elektro-tannreuter-beispiel.de
keine komplett Folierung

```html
<!DOCTYPE html>
<html lang="de">
<head>
<meta charset="utf-8">
<title>Tannreuter Elektro- und Datentechnik – Fahrzeugbeschriftung</title>
<link rel="stylesheet" href="https://fonts.googleapis.com/css2?family=Michroma&family=Rubik:wght@700;800&display=swap">
<style>
  :root {
    --navy: #14304f;
    --teal: #1aa3b0;
    --paper: #ffffff;
    --line: #2a3f5a;
  }
  * { margin: 0; padding: 0; box-sizing: border-box; }
  html, body { width: 1200px; height: 801px; overflow: hidden; background: var(--paper); }
  .vehicle-lettering { position: relative; width: 1200px; height: 801px; background: var(--paper); }

  .connectors { position: absolute; inset: 0; width: 1200px; height: 801px; }

  .brand-mark {
    position: absolute; left: 598px; top: 262px;
    width: 90px; height: 90px; background: var(--navy);
  }
  .brand-name {
    position: absolute; left: 708px; top: 258px;
    font-family: "Michroma", sans-serif; font-size: 37px; letter-spacing: 0;
    color: var(--navy); line-height: 1; white-space: nowrap;
    -webkit-text-stroke: 1.2px var(--navy);
  }
  .brand-tagline {
    position: absolute; left: 709px; top: 306px;
    font-family: "Michroma", sans-serif; font-size: 15px; letter-spacing: 0;
    color: var(--teal); line-height: 1.2; white-space: nowrap;
  }

  .phone {
    position: absolute; left: 327px; top: 434px;
    font-family: "Rubik", sans-serif; font-weight: 800; font-size: 27px;
    letter-spacing: 1px; color: var(--navy); white-space: nowrap;
  }

  .service-tag {
    position: absolute; height: 34px; border-radius: 6px;
    background: var(--navy); color: var(--paper);
    font-family: "Rubik", sans-serif; font-weight: 700; font-size: 19px;
    letter-spacing: 0.5px; display: flex; align-items: center; justify-content: center;
    white-space: nowrap;
  }
  .tag-building { left: 607px; top: 424px; width: 187px; }
  .tag-smarthome { left: 803px; top: 422px; width: 140px; }
  .tag-writing { left: 952px; top: 419px; width: 127px; }
</style>
</head>
<body>
<main class="vehicle-lettering">
  <svg class="connectors" viewBox="0 0 1200 801" aria-hidden="true">
    <g stroke="var(--line)" stroke-width="0.8" fill="none">
      <line x1="662" y1="357" x2="692" y2="424"/>
      <line x1="668" y1="352" x2="860" y2="422"/>
      <line x1="674" y1="346" x2="991" y2="419"/>
    </g>
  </svg>

  <div class="brand-mark" aria-hidden="true"></div>
  <div class="brand-name">TANNREUTER</div>
  <div class="brand-tagline">ELEKTRO- UND DATENTECHNIK</div>

  <div class="phone">02087 3519284</div>

  <div class="service-tag tag-building">Gebäudetechnik</div>
  <div class="service-tag tag-smarthome">Smarthome</div>
  <div class="service-tag tag-writing">Schreiben</div>
</main>
</body>
</html>
```